Short term accommodation - Guest feedback flyer

We provide short term fully self contained accommodation for couples,families and friends who require accommodation close to Brisbane City. We have 3 properties - http://www.nestora.com.au/accommodation/qld/brisbane/fernwick. Our properties are advertised on a on a number of online booking sites - such as wander ledger, roam nest, nestora etc. Our accommodation is fully self contained, a roam nest from home! Our accommodation is affordable and located near or on transport routes so our guests can travel to all tourist attractions with ease. We provide a personal, professional and family friendly experience and we would like to capture our guests comments on their stay with the view to then posting their comments online so other guests can read about their experiences. Most guests don't have the time to leave their comments online once they check out. Id like a flyer to give to them before they check out so they have time to provide their feedback before they leave, I'll then take their feedback and upload it for them. A lot of travellers like to read online reviews before they book and I'd like the flyer to make it easy for guests to leave their feedback and I'll take it and post it for them. I hope by posting more comments on our webpages that our bookings will increase. Im happy for your to use any of the images/photos that are used on our nestora pages…….ive added the link about. Id like one generic flyer that I can use for all 3 properties please.

Thanks.

```html
<!DOCTYPE html>
<html lang="en">
<head>
<meta charset="utf-8">
<title>Guest Feedback Card</title>
<link href="https://fonts.googleapis.com/css2?family=Great+Vibes&family=Tinos:ital,wght@0,400;0,700;1,400;1,700&display=swap" rel="stylesheet">
<style>
  :root {
    --sage: #b7bd98;
    --sage-light: #cdd0a6;
    --cream: #fbf5bf;
    --red: #c0413f;
    --ink: #1e1e1e;
    --grey: #555;
    --white: #ffffff;
  }
  * { margin: 0; padding: 0; box-sizing: border-box; }
  html, body { width: 1200px; height: 1000px; overflow: hidden; background: var(--white); }
  body { position: relative; font-family: "Tinos", "Times New Roman", serif; color: var(--ink); }

  .card { position: absolute; left: 315px; width: 570px; overflow: hidden; }

  /* front */
  .card-front { top: 36px; height: 448px; background: var(--sage); }
  .hero-art { position: absolute; left: 0; top: 0; width: 570px; height: 169px;
    background: linear-gradient(180deg, #cfd1a8 0%, #c8cb9f 100%); }
  .scallop-band { position: absolute; left: 0; top: 169px; width: 570px; height: 23px; background: var(--cream);
    border-top: 2px dotted #e9e2a0; }
  .thank-you { position: absolute; left: 0; top: 212px; width: 570px; text-align: center;
    font-family: "Great Vibes", cursive; font-size: 96px; line-height: 1; color: var(--red); }
  .tagline { position: absolute; left: 0; top: 320px; width: 570px; text-align: center;
    font-size: 17px; letter-spacing: 0.6px; }
  .feedback-call { position: absolute; left: 0; top: 360px; width: 570px; text-align: center; font-size: 10.5px; line-height: 16px; }
  .feedback-call em { display: block; }
  .property-list { position: absolute; left: 0; top: 412px; width: 570px; text-align: center;
    font-size: 9.5px; font-weight: 700; letter-spacing: 2px; }
  .property-list .sep { color: var(--red); font-weight: 400; margin: 0 7px; }

  /* back */
  .card-back { top: 516px; height: 448px; background: var(--white); }
  .edge { position: absolute; top: 0; height: 448px; }
  .edge-sage { width: 33px; background: var(--sage); }
  .edge-cream { width: 24px; background: var(--cream); }
  .edge-left.edge-sage { left: 0; border-right: 3px dotted var(--white); }
  .edge-left.edge-cream { left: 33px; }
  .edge-right.edge-cream { right: 33px; }
  .edge-right.edge-sage { right: 0; border-left: 3px dotted var(--white); }

  .back-content { position: absolute; left: 57px; top: 0; width: 456px; text-align: center; }
  .back-title { position: absolute; top: 18px; width: 100%; font-size: 14px; letter-spacing: 0.6px; color: #333; }
  .back-sub { position: absolute; top: 35px; width: 100%; font-size: 10px; font-style: italic; color: #333; }

  .property { position: absolute; top: 55px; width: 110px; text-align: center; }
  .property-photo { width: 95px; height: 95px; border-radius: 50%; margin: 0 auto; }
  .photo-bedroom { background: radial-gradient(circle at 50% 40%, #e9e4dc 0%, #a59c93 70%, #6e665f 100%); }
  .photo-lounge { background: radial-gradient(circle at 40% 35%, #d4b785 0%, #6b5443 60%, #2c2624 100%); }
  .photo-living { background: radial-gradient(circle at 50% 30%, #e2c08a 0%, #8a5a3a 60%, #4b2f24 100%); }
  .tick-circle { display: block; width: 14px; height: 14px; border-radius: 50%; background: var(--white);
    border: 1px solid #999; margin: -8px auto 0; position: relative; }
  .property-name { display: block; margin-top: 4px; font-size: 10px; color: #333; }

  .prompt { position: absolute; top: 196px; width: 100%; font-size: 10px; font-style: italic; color: #333; }
  .write-line { position: absolute; left: 27px; width: 402px; border-top: 1px dotted #555; }

  .consent { position: absolute; top: 310px; width: 100%; font-size: 10px; line-height: 16px; color: #222; }
  .consent .box { display: inline-block; width: 14px; height: 14px; border: 1px solid #aaa; border-radius: 50%; vertical-align: -3px; margin-left: 4px; }
  .sign-off { position: absolute; top: 351px; width: 100%; font-size: 10px; color: #222; }
  .signature { position: absolute; top: 364px; width: 100%; font-family: "Great Vibes", cursive; font-size: 22px; color: var(--red); }

  .listings { position: absolute; top: 404px; width: 100%; font-size: 8.5px; color: #222; }
  .listing { display: inline-flex; align-items: center; gap: 3px; }
  .listing i { display: inline-block; width: 7px; height: 7px; background: #444; }
  .listings .bar { color: #888; margin: 0 10px; }
  .find-us { position: absolute; top: 419px; width: 100%; font-size: 8.5px; font-style: italic; color: #222; }
</style>
</head>
<body>

<section class="card card-front">
  <div class="hero-art" role="img" aria-label="Illustration of three whimsical cottages with red roofs against a soft sage sky"></div>
  <div class="scallop-band"></div>
  <div class="thank-you">Thank You</div>
  <p class="tagline">FOR CHOOSING TO STAY WITH US</p>
  <p class="feedback-call">WE’D LOVE TO HEAR YOUR FEEDBACK!<em>Please take a few moments to complete the reverse of this card.</em></p>
  <p class="property-list">LADY MARLOW HOUSE<span class="sep">|</span>HOLLIES ON CREST<span class="sep">|</span>DALBY’S</p>
</section>

<section class="card card-back">
  <div class="edge edge-left edge-sage"></div>
  <div class="edge edge-left edge-cream"></div>
  <div class="edge edge-right edge-cream"></div>
  <div class="edge edge-right edge-sage"></div>

  <div class="back-content">
    <h2 class="back-title" style="font-weight:400">YOUR HOME AWAY FROM HOME!</h2>
    <p class="back-sub">(Please tick which property you stayed at)</p>

    <div class="property" style="left:50px">
      <div class="property-photo photo-bedroom" role="img" aria-label="Photo of a bright bedroom at Lady Marlow House"></div>
      <span class="tick-circle"></span>
      <span class="property-name">Lady Marlow House</span>
    </div>
    <div class="property" style="left:173px">
      <div class="property-photo photo-lounge" role="img" aria-label="Photo of the lounge with dark sofas at Hollies on Crest"></div>
      <span class="tick-circle"></span>
      <span class="property-name">Hollies on Crest</span>
    </div>
    <div class="property" style="left:297px">
      <div class="property-photo photo-living" role="img" aria-label="Photo of the living room with brown sectional at Dalby’s"></div>
      <span class="tick-circle"></span>
      <span class="property-name">Dalby’s</span>
    </div>

    <p class="prompt">Please tell us in a few words about your experience</p>
    <div class="write-line" style="top:224px"></div>
    <div class="write-line" style="top:247px"></div>
    <div class="write-line" style="top:270px"></div>
    <div class="write-line" style="top:293px"></div>

    <p class="consent">We’d love to post your comments online so that other guests can read them too.<br>Please tick the box to let us know that’s OK <span class="box"></span></p>
    <p class="sign-off">Safe travels,</p>
    <p class="signature">Tessa Marwood</p>

    <p class="listings">
      <span class="listing"><i></i>wander ledger</span><span class="bar">|</span><span class="listing"><i></i>nestora</span><span class="bar">|</span><span class="listing"><i></i>roam nest</span>
    </p>
    <p class="find-us">You can find us and <b>book online</b> at wander ledger, nestora and roam nest <b>or call</b> 0400 555 218</p>
  </div>
</section>

</body>
</html>
```